Weight gainer supplement design

Looking for a design for a weight gainer /meal replacement supplement. The black plastic tub we will use has 2 spaces for sticker one around the rim approx 2.8cm tall x 30cm wideAnother around the main tub. The main sticker size will be 18cm tall by 70cm this will include the front of the product then wrap around to show the nutritional table.The brand is KTV (Kestrel training vitals) and the product will be called ALPHA MASSThe target ordience is men aged 16-35 its should have a profesional feel to it. The product comes in a black tub, the colores we would like to use are black and blue or red or gold or silver but we are open to suggestions and would like artistic imput. Are logo for KTV is attached but can be changed if the designer prefers.Attached is 1. KTV logo2. Image of similar product that comes in the same tub3 - 5 - images of similar products that we like the design of.The product is 12lbs and will be vanilla flavor. Please ask for more suggestions if needed, I have kept this description short to try and get artistic input.Thanks in advance :)
Updates

Target Market(s)

18-35 males who go to the gym

Industry/Entity Type

Fitness

Colors

Designer to choose colors to be used in the design.

Requirements
Must have
• name bravo bulk, logo KTV
Should not have
• images of people

```html
<!DOCTYPE html>
<html lang="en">
<head>
<meta charset="utf-8">
<title>Bravo Bulk – Vanilla Tub Label</title>
<link rel="stylesheet" href="https://fonts.googleapis.com/css2?family=Open+Sans:wght@300;400;600;700;800&family=Oswald:wght@600&display=swap">
<style>
  :root {
    --navy-top: #1f3555;
    --ink: #141a27;
    --ink-soft: #1b2334;
    --steel-blue: #263d62;
    --night: #121a2c;
    --red: #db1f3c;
    --red-bright: #ef3b50;
    --white: #ffffff;
    --mist: #e9ebed;
    --grey-text: #6c7380;
    --label-black: #111111;
    --vanilla: #f3dd8a;
    --vanilla-pod: #4a3020;
  }
  * { box-sizing: border-box; margin: 0; padding: 0; }
  html, body { width: 1200px; height: 309px; overflow: hidden; background: var(--white); }
  body { font-family: "Open Sans", Arial, sans-serif; }

  .label { position: relative; width: 1200px; height: 309px; overflow: hidden; }
  .label__shapes { position: absolute; inset: 0; }

  .benefits { position: absolute; left: 42px; top: 44px; color: var(--white); }
  .benefits__title { font-size: 10px; font-weight: 700; letter-spacing: .4px; margin-bottom: 4px; }
  .benefits__list { list-style: none; }
  .benefits__list li { font-size: 7.6px; font-weight: 600; letter-spacing: .4px; line-height: 13px; padding-left: 11px; position: relative; }
  .benefits__list li::before { content: ""; position: absolute; left: 0; top: 5px; width: 3.5px; height: 3.5px; border-radius: 50%; background: var(--white); }

  .weight-badge { position: absolute; left: 56px; top: 176px; width: 88px; height: 40px; }
  .weight-badge__ribbon { position: absolute; left: 0; top: 10px; width: 70px; height: 18px; background: var(--red); transform: skewX(-25deg); }
  .weight-badge__circle { position: absolute; left: 28px; top: 2px; width: 36px; height: 36px; border-radius: 50%; background: var(--night); border: 2px solid var(--white); color: var(--white); font-weight: 800; font-size: 17px; line-height: 32px; text-align: center; }
  .weight-badge__unit { position: absolute; left: 55px; top: 20px; background: var(--red); color: var(--white); font-weight: 700; font-size: 9px; padding: 1px 4px; }

  .website { position: absolute; left: 60px; top: 234px; color: #c9ced6; font-size: 9px; letter-spacing: .3px; }

  .flavour-word { position: absolute; left: 292px; top: 160px; transform: translate(-50%, -50%) rotate(-90deg); font-size: 30px; font-weight: 300; letter-spacing: 11px; color: #3c4352; white-space: nowrap; }

  .flavour-art { position: absolute; left: 344px; top: 172px; width: 56px; height: 40px; border-radius: 50%; background: radial-gradient(circle at 55% 45%, var(--vanilla) 0 35%, #d9b85a 55%, var(--vanilla-pod) 75%, transparent 76%); }

  .product-name { position: absolute; left: 412px; top: 88px; line-height: 1; }
  .product-name__main { display: block; font-size: 64px; font-weight: 700; color: var(--white); letter-spacing: -1.5px; text-shadow: 2px 3px 6px rgba(0,0,0,.45); }
  .product-name__sub { display: block; font-size: 46px; font-weight: 400; color: var(--red); letter-spacing: -1px; margin: -4px 0 0 56px; }

  .new-stamp { position: absolute; left: 577px; top: 219px; width: 60px; height: 22px; border: 2px solid var(--white); color: var(--white); font-family: "Oswald", "Arial Narrow", sans-serif; font-size: 15px; font-weight: 600; line-height: 18px; text-align: center; letter-spacing: 1px; }

  .brand-mark { position: absolute; left: 806px; top: 214px; display: flex; align-items: center; gap: 6px; }
  .brand-mark__square { width: 12px; height: 12px; background: var(--red); }
  .brand-mark__name { font-size: 30px; font-weight: 800; color: var(--red); letter-spacing: 1px; line-height: 1; }

  .nutrition { position: absolute; left: 950px; top: 50px; width: 156px; background: var(--white); border: 1px solid var(--label-black); padding: 2px 3px; color: var(--label-black); font-size: 3.4px; line-height: 1.35; }
  .nutrition__title { font-size: 11.5px; font-weight: 800; line-height: 1.1; border-bottom: 3px solid var(--label-black); padding-bottom: 1px; }
  .nutrition__meta { display: flex; justify-content: space-between; font-weight: 700; padding: 1px 0; border-bottom: 2px solid var(--label-black); }
  .nutrition__meta span:last-child { text-align: right; }
  .nutrition__table { width: 100%; border-collapse: collapse; }
  .nutrition__table td { border-bottom: .4px solid #999; padding: .3px 1px; }
  .nutrition__table td:last-child { text-align: right; }
  .nutrition__table .indent td:first-child { padding-left: 6px; }
  .nutrition__head td { font-weight: 700; text-align: right; }
  .nutrition__section { font-weight: 700; border-top: 2px solid var(--label-black); padding-top: 1px; }
  .amino { width: 100%; border-collapse: collapse; margin-bottom: 2px; }
  .amino th, .amino td { border: .4px solid #999; padding: .2px 1px; text-align: left; }
  .amino th { font-weight: 700; }
  .amino td:nth-child(2n) { text-align: right; }
  .nutrition p { border-top: .6px solid var(--label-black); padding: 1px 0; }
  .nutrition b { font-weight: 700; }
  .nutrition__warning { border: .8px solid var(--label-black); padding: 1px 2px; margin-top: 2px; }
</style>
</head>
<body>
<main class="label">
  <svg class="label__shapes" viewBox="0 0 1500 386" width="1200" height="309" aria-hidden="true">
    <defs>
      <radialGradient id="mist-fill" cx="70%" cy="45%" r="70%">
        <stop offset="0" stop-color="#c9ccd0"/>
        <stop offset=".45" stop-color="#e6e8ea"/>
        <stop offset="1" stop-color="#fbfbfb"/>
      </radialGradient>
    </defs>
    <rect class="shape-base" width="1500" height="386" fill="var(--ink)"/>
    <polygon class="shape-shade" points="300,22 420,22 560,362 440,362" fill="var(--ink-soft)"/>
    <polygon class="shape-blue" points="420,22 640,22 800,362 560,362" fill="var(--steel-blue)"/>
    <polygon class="shape-night" points="640,22 710,22 870,362 800,362" fill="var(--night)"/>
    <polygon class="shape-red" points="710,22 775,22 920,362 870,362" fill="var(--red)"/>
    <polygon class="shape-red-bright" points="775,22 840,22 960,362 920,362" fill="var(--red-bright)"/>
    <polygon class="shape-mist" points="840,22 1500,22 1500,362 960,362" fill="url(#mist-fill)" role="img" aria-label="Soft blurred grey backdrop"/>
    <rect class="band-top" width="1500" height="22" fill="var(--navy-top)"/>
    <rect class="band-bottom" y="362" width="1500" height="24" fill="var(--red)"/>
  </svg>

  <section class="benefits">
    <h2 class="benefits__title">Lorem ipsum Dolor</h2>
    <ul class="benefits__list">
      <li>Lorem ipsum dolor point</li>
      <li>Interdum et malesuada fames point</li>
      <li>Vivamus porta hendrerit nisi point</li>
      <li>Lorem ipsum dolor point</li>
      <li>Interdum et malesuada fames point</li>
      <li>Vivamus porta hendrerit nisi point</li>
    </ul>
  </section>

  <div class="weight-badge">
    <div class="weight-badge__ribbon"></div>
    <div class="weight-badge__circle">12</div>
    <div class="weight-badge__unit">LB</div>
  </div>

  <div class="website">www.kestrelvitals.com</div>

  <div class="flavour-word">VANILLA</div>
  <div class="flavour-art" role="img" aria-label="Vanilla flower with vanilla pods"></div>

  <h1 class="product-name">
    <span class="product-name__main">BRAVO</span>
    <span class="product-name__sub">BULK</span>
  </h1>

  <div class="new-stamp">NEW</div>

  <div class="brand-mark">
    <span class="brand-mark__square"></span>
    <span class="brand-mark__name">KTV</span>
  </div>

  <section class="nutrition">
    <h3 class="nutrition__title">Nutrition Information</h3>
    <div class="nutrition__meta">
      <span>Serving Size: 3 Scoops (227g)<br>Servings Per Container: 24</span>
      <span>Content: 5443 grams<br>NET WT: 192 oz / 12 lb</span>
    </div>
    <table class="nutrition__table">
      <tr class="nutrition__head"><td></td><td>Per Serving</td></tr>
      <tr><td>Energy</td><td>3598 kJ / 860 kcal</td></tr>
      <tr><td>Fat</td><td>7g</td></tr>
      <tr class="indent"><td>Of which saturates</td><td>2g</td></tr>
      <tr><td>Carbohydrates</td><td>145g</td></tr>
      <tr class="indent"><td>Of which sugars</td><td>9g</td></tr>
      <tr><td>Protein</td><td>51g</td></tr>
      <tr><td>Salt</td><td>0.5g</td></tr>
    </table>
    <div class="nutrition__section">Typical Amino Acid Profile (Milligrams Per Serving)</div>
    <table class="amino">
      <tr><th colspan="2">Essential Amino Acids</th><th colspan="2">Conditional Amino Acids</th><th colspan="2">Other Amino Acids</th></tr>
      <tr><td>Isoleucine</td><td>2365</td><td>Glutamine</td><td>8590</td><td>Aspartic Acid</td><td>5612</td></tr>
      <tr><td>Leucine</td><td>5045</td><td>Arginine</td><td>1578</td><td>Serine</td><td>2714</td></tr>
      <tr><td>Valine</td><td>2495</td><td>Histidine</td><td>952</td><td>Glycine</td><td>980</td></tr>
      <tr><td>Tryptophan</td><td>639</td><td>Cystine</td><td>1286</td><td>Alanine</td><td>2602</td></tr>
      <tr><td>Lysine</td><td>4663</td><td>Tyrosine</td><td>1769</td><td></td><td></td></tr>
      <tr><td>Threonine</td><td>3618</td><td>Proline</td><td>2430</td><td></td><td></td></tr>
      <tr><td>Phenylalanine</td><td>1629</td><td></td><td></td><td></td><td></td></tr>
      <tr><td>Methionine</td><td>1158</td><td></td><td></td><td></td><td></td></tr>
    </table>
    <p><b>Ingredients:</b> waxy maize, whey protein blend (whey protein concentrate, whey protein isolate), oat flour, flavouring, sweetener (sucralose), thickener (xanthan gum).</p>
    <p><b>Additional Information:</b> this gainer is based on servings of 227 grams, containing 51 grams protein. Values may show slight deviation per batch.</p>
    <p><b>Suggested Use:</b> add 3 scoops to 700 ml of cold water. Shake for 15 seconds and enjoy. Take 1 or 2 servings daily.</p>
    <div class="nutrition__warning"><b>Warning:</b> This is a food supplement. It should not be used as a substitute for a varied diet. Store in a cool, dry place out of reach of children. Do not exceed the recommended dose. Batch number and expiry date are displayed at the back of this product.</div>
  </section>
</main>
</body>
</html>
```